My Professional Resume/CV Design

Hi Pixel Harbor experts, I need a professional resume/CV design for using my carrier hiring activities. I have a draft and this draft is 2 types.
1) Traditional IT Major Company Senior(Manager Level) to Director level application (File: Tanabe_Emiko_Res_EN2023AprA)
>Application example companies: Velmora, Drakt, Quindle, Brightmarsh, HoltenWare, Fenwick Ridge, Zentravix, Morivon, Quorexa, Plinth, dZop, Kelvarna etc
>This should not be fancy. Please make format with traditional/gentle/standard but also need to appear unique point such as icons, borderlines etc
2) Cutting-Edge (Web 3.0/metaverse/NFT/Crypto) Start-up or Young (Less 5 year's history) Company Director and C-Levels position application (Tanabe_Emiko_Res_EN2023Apr_typeC)
>Application Example Companies: Tessaluk Studios, Vorlexa, Zintaro.example, Wovenpath, Lumbrook, FernPocket, Thaxel, Kipa/Dult/Snov, Morvik, QUESTAN, wordLYM etc
>This resume format should be something "edge" "advanced" "future" and "high-tech", so need to your high sense of design technics.
Both drafts is without a profile picture, but I need to put in my portfolio picture (Just attached one is my 2018's, you can trim and edit as well)
For the document format, please send me to WORD and PAGES both. and total MAX 2 page in all contents please (No more 3 pages)
Target Market(s)
Traditional Major Tech Company's VP/Directors or/and Latest Web 3.0 StartUp C-Levels (CEO/CTO/CSO/COO etc)
Industry/Entity Type
Technology
Font styles to use
Other font styles liked:
- Choose 3 a)Century Gothic b) Avenir c)Graphik d)Kohinoor e)Optima f)Platino
Look and feel
Each slider illustrates characteristics of the customer's brand and the style your logo design should communicate.

```html
<!DOCTYPE html>
<html lang="en">
<head>
<meta charset="utf-8">
<title>Emiko Tanabe – Resume</title>
<link href="https://fonts.googleapis.com/css2?family=Arimo:wght@400&family=Didact+Gothic&display=swap" rel="stylesheet">
<style>
:root{
  --purple:#9c4a9f;
  --charcoal:#58595b;
  --grey:#8b8b8b;
  --ink:#111111;
  --paper:#ffffff;
}
*{margin:0;padding:0;box-sizing:border-box}
html,body{width:888px;height:1200px;overflow:hidden;background:var(--paper)}
body{position:relative;font-family:"Arimo",Arial,sans-serif;color:var(--grey)}
.brand{position:absolute;left:61px;top:49px;display:flex;align-items:center;gap:10px}
.brand-mark{width:86px;height:86px;border-radius:50%;border:1.5px solid var(--charcoal);background:var(--charcoal)}
.brand-name{font-family:"Didact Gothic","Century Gothic",sans-serif;font-size:37px;line-height:35px;color:var(--charcoal)}
.contact{position:absolute;right:76px;top:76px;font-size:15.5px;color:var(--charcoal);letter-spacing:.1px}
.contact a{color:var(--grey);text-decoration:underline}
.contact .sep{margin:0 6px}
.rule{position:absolute;left:60px;top:155px;width:766px;height:5px;border-top:2px solid var(--purple);border-bottom:2px solid var(--purple)}
.portrait{position:absolute;left:55px;top:185px;width:195px;height:195px;border-radius:50%;border:1px solid var(--purple);background:radial-gradient(circle at 50% 40%,#6d6d6d,#1c1c1c 70%)}
.section-title{font-size:13.6px;color:var(--purple);letter-spacing:.2px}
.dots{display:flex;margin:6px 0 5px}
.dots span{width:11px;height:11px;border-radius:50%}
.dots span:first-child{background:var(--charcoal)}
.dots span:last-child{background:var(--purple);margin-left:-2px}
.profile{position:absolute;left:268px;top:184px;width:560px;font-size:13.3px;line-height:19.2px}
.profile p+p{margin-top:19px}
.competencies{position:absolute;left:75px;top:418px;width:750px}
.competencies .intro{font-size:13.4px;line-height:19.6px;color:var(--ink)}
.skill-grid{display:flex;margin-top:19px}
.skill-list{list-style:none;font-size:13.3px;line-height:20.4px}
.skill-list li{position:relative;padding-left:29px}
.skill-list li::before{content:"";position:absolute;left:2px;top:8px;width:5px;height:5px;border-radius:50%;background:#9a9a9a}
.skill-list.left{width:380px;padding-right:12px}
.skill-list.right{width:375px}
.career{position:absolute;left:75px;top:958px;width:750px}
.career-grid{display:flex}
.role-list{list-style:none;font-size:13.3px;line-height:20.4px}
.role-list li{position:relative;padding-left:29px;margin-bottom:0}
.role-list li::before{content:"";position:absolute;left:2px;top:8px;width:5px;height:5px;border-radius:50%;background:#555}
.role-list .company{color:var(--ink)}
.role-list .title{color:var(--grey)}
.role-list.left{width:380px}
.role-list.right{width:370px}
</style>
</head>
<body>
<header>
  <div class="brand">
    <div class="brand-mark"></div>
    <div class="brand-name">Emiko<br>Tanabe</div>
  </div>
  <div class="contact">Wanchai, Hong Kong<span class="sep">|</span><a href="mailto:etanabe512@example.com">etanabe512@example.com</a><span class="sep">|</span>+852 5550 0123</div>
  <div class="rule"></div>
</header>

<div class="portrait" role="img" aria-label="Portrait photograph of Emiko Tanabe"></div>

<section class="profile">
  <h2 class="section-title">PROFESSIONAL PROFILE:</h2>
  <div class="dots"><span></span><span></span></div>
  <p>As an experienced professional, I have a growth-oriented mindset and a strong understanding of current marketing tools, strategies, and cutting-edge technology.</p>
  <p>I am skilled in collaborating with external vendors and internal business partners to develop and execute marketing strategies that align with our business growth plans. I have expertise in evaluating customer experience across various channels and touchpoints, and I am analytical in my approach. I also demonstrate creativity in identifying target audiences and developing digital campaigns, while still valuing traditional engagement methods.</p>
</section>

<section class="competencies">
  <h2 class="section-title">CORE COMPETENCIES:</h2>
  <div class="dots"><span></span><span></span></div>
  <p class="intro">As a native Japanese fluent in English and familiar with business practices both in Japan and internationally, I can help non-Japanese companies enter the Japanese market by bridging the cultural gap. With my expertise in marketing research and data analysis, I can lead digital and offline marketing campaigns and serve as a supply chain interface for major projects. I also have experience in developing brand and product marketing plans and campaigns for companies and business lines. Here are my top competencies:</p>
  <div class="skill-grid">
    <ul class="skill-list left">
      <li>Global operations management</li>
      <li>Strategic partnerships development and management</li>
      <li>Process improvement champion with a focus on continuous improvement</li>
      <li>Strategic planning and execution for achieving organizational goals and objectives</li>
      <li>Cryptocurrency expertise with experience in both B2B and B2C markets</li>
      <li>Research and development for new products, services, and markets</li>
      <li>Key account management for maintaining strong relationships with important clients</li>
      <li>Business restructuring for enhancing organizational efficiency and effectiveness</li>
      <li>Team leadership and management to motivate and guide employees towards achieving common goals</li>
    </ul>
    <ul class="skill-list right">
      <li>P&amp;L management and revenue growth to increase profitability and sustainability</li>
      <li>Budget management to ensure financial stability and optimize resource allocation</li>
      <li>Sales experience in B2B and B2G markets</li>
      <li>Staff training and retention to enhance employee productivity and engagement</li>
      <li>Business administration to ensure compliance with regulations and legal requirements</li>
      <li>Supply chain and logistics management for efficient and effective movement of goods and services</li>
      <li>Vendor and financial management for effective management of external relationships</li>
      <li>Negotiation and agreement skills for ensuring favorable deals and contracts</li>
      <li>Records and documentation management to ensure compliance and accountability</li>
    </ul>
  </div>
</section>

<section class="career">
  <h2 class="section-title">CAREER HIGHLIGHTS:</h2>
  <div class="dots"><span></span><span></span></div>
  <div class="career-grid">
    <ul class="role-list left">
      <li><div class="company">Cudaline Networks, Hong Kong</div><div class="title">Inside Renewal Sales</div></li>
      <li><div class="company">Norrel HK Limited, Hong Kong</div><div class="title">Business Development Manager</div></li>
      <li><div class="company">Pelvo High-Tech Limited, Hong Kong</div><div class="title">Advisor, Business Development</div></li>
      <li><div class="company">Tarrow Global, Hong Kong</div><div class="title">Business Development Manager</div></li>
    </ul>
    <ul class="role-list right">
      <li><div class="company">Corelane Tech Limited (Bramfield Group (Holdings) Ltd., Hong Kong</div><div class="title">Head of Division</div></li>
      <li><div class="company">PT. Sarika Bali, Tokyo &amp; Denpasar</div><div class="title">Project Manager</div></li>
      <li><div class="company">Meridia Agency, Tokyo</div><div class="title">Chief Operations Officer</div></li>
    </ul>
  </div>
</section>
</body>
</html>
```